Strong, modern, clean Business Card design

Looking for a stunning, but CLEAN business card design. While we are a faith-based organization, we do NOT want this to look religious.

Industry/Entity Type

Non-Profit

Contact Information for Business Card

Dale Munroe | Lead Pastor
dale@BrightHarvestHope.org
970-555-0148
PO Box 7316
Ashford, WY 80571

Font styles to use
Serif
Sans Serif

Requirements
Should not have
• Religious imagery or symbolism

```html
<!DOCTYPE html>
<html lang="en">
<head>
<meta charset="utf-8">
<title>Harvest Hope Church – Dale Munroe</title>
<link rel="stylesheet" href="https://fonts.googleapis.com/css2?family=Arimo&family=Cinzel:wght@400&family=Crimson+Text&family=Open+Sans:ital@1&display=swap">
<style>
  :root {
    --ink: #1b1b1b;
    --paper: #ffffff;
    --accent: #ff0000;
    --edge: #d9d9d9;
    --brand: #2a1f1f;
  }
  html, body {
    margin: 0;
    padding: 0;
    width: 1200px;
    height: 687px;
    overflow: hidden;
    background: var(--paper);
  }
  .business-card {
    display: block;
    width: 1200px;
    height: 687px;
  }
  .card-base { fill: var(--paper); stroke: var(--edge); stroke-width: 2; }
  .side-bar, .contact-panel, .brand-dot { fill: var(--ink); }
  .accent { fill: var(--accent); }
  .brand-name {
    font-family: "Cinzel", Georgia, serif;
    font-weight: 400;
    fill: var(--brand);
  }
  .brand-name-top { font-size: 76px; letter-spacing: 2px; }
  .brand-name-bottom { font-size: 50px; letter-spacing: 26px; }
  .person-name {
    font-family: "Crimson Text", Georgia, serif;
    font-size: 66px;
    fill: #000;
  }
  .person-role {
    font-family: "Open Sans", Arial, sans-serif;
    font-style: italic;
    font-size: 31px;
    letter-spacing: 1px;
    fill: var(--ink);
  }
  .contact-line {
    font-family: "Arimo", Arial, sans-serif;
    font-size: 42px;
    fill: var(--paper);
  }
  .contact-email { font-size: 37px; }
</style>
</head>
<body>
<svg class="business-card" viewBox="0 0 1200 687" xmlns="http://www.w3.org/2000/svg">
  <rect class="card-base" x="1" y="1" width="1198" height="685"/>

  <rect class="side-bar" x="0" y="0" width="32" height="687"/>
  <rect class="side-bar" x="1168" y="0" width="32" height="687"/>

  <circle class="brand-dot" cx="190" cy="155" r="125"/>
  <text class="brand-name brand-name-top" x="357" y="177">HARVEST HOPE</text>
  <text class="brand-name brand-name-bottom" x="456" y="265">CHURCH</text>

  <polygon class="accent" points="32,479 82,522 32,566"/>
  <text class="person-name" x="311" y="545" text-anchor="middle">Dale Munroe</text>
  <text class="person-role" x="311" y="590" text-anchor="middle">Lead Pastor</text>

  <path class="contact-panel" d="M640 325 H1168 V653 H770 Q730 653 718 618 L620 356 Q610 325 640 325 Z"/>
  <rect class="accent" x="1170" y="325" width="28" height="328"/>

  <text class="contact-line contact-email" x="1154" y="391" text-anchor="end">dale@BrightHarvestHope.org</text>
  <text class="contact-line" x="1154" y="468" text-anchor="end">Ashford, WY 80571</text>
  <text class="contact-line" x="1154" y="548" text-anchor="end">970-555-0148</text>
  <text class="contact-line" x="1154" y="622" text-anchor="end">PO Box 7316</text>
</svg>
</body>
</html>
```